Need a vitamin/supplement label

Hi,
I need a vitamin label designing for a product that will be sold online.
The label needs to have the following information on the front:
1) B12
2) Methycobalamin
3) 1000mcg
4) 90 Lozenges
5) Sublingual
6) Dietary Supplement
7) Vegetarian
Numbers 1 and 2 need to standout the most because the product will only be sold online so visibility is key.
Use this design as an inspiration:
http://www.shopverdiq.example/Tolvane-Nutrics-Methylcobalamin-5000mcg-Lozenges/dp/K7724PLMZ3/ref=sr_1_2?ie=UTF8&qid=4928163507&sr=8-2&keywords=b12
The label should come across as premium.
The brand name is 'Corlen Sabo' and I haven't had a logo designed so there's some freedom when it comes to that. It needs to be simple and clean.
If you need any clarifications then let me know.
Online

```html
<!DOCTYPE html>
<html lang="en">
<head>
<meta charset="utf-8">
<title>Corlen Sabo B-12 Methycobalamin Label</title>
<link rel="stylesheet" href="https://fonts.googleapis.com/css2?family=Arimo:ital,wght@0,400;0,700;1,700&family=Tinos&display=swap">
<style>
  :root {
    --backdrop: #e6e6e6;
    --label-white: #ffffff;
    --brand-orange: #f07a20;
    --brand-orange-deep: #e0651a;
    --text-orange: #d9621a;
    --ink-grey: #4a4a4a;
    --band-grey-light: #a9a9a9;
    --band-grey-dark: #6b6b6b;
    --rule-grey: #7a7a7a;
  }
  * { margin: 0; padding: 0; box-sizing: border-box; }
  html, body {
    width: 1200px; height: 960px; overflow: hidden;
    background: var(--backdrop);
  }
  .label {
    position: absolute; left: 340px; top: 240px;
    width: 500px; height: 620px;
    background: var(--label-white);
    font-family: "Arimo", Arial, sans-serif;
    overflow: hidden;
  }
  .brand-tab {
    position: absolute; left: 0; top: 52px;
    width: 108px; height: 34px;
    background: var(--brand-orange);
  }
  .brand-mark {
    position: absolute; left: 120px; top: 60px;
    width: 18px; height: 18px;
    background: var(--brand-orange-deep);
  }
  .brand-name {
    position: absolute; left: 148px; top: 50px;
    font-family: "Tinos", "Times New Roman", serif;
    font-size: 36px; line-height: 1;
    color: var(--text-orange);
    white-space: nowrap;
  }
  .claim {
    position: absolute; left: 40px; top: 140px; width: 300px;
    font-style: italic; font-weight: 700;
    font-size: 22px; line-height: 30px;
    color: var(--ink-grey); text-align: right;
  }
  .brain-art {
    position: absolute; left: 325px; top: 92px;
    width: 160px; height: 140px; border-radius: 50%;
    background: radial-gradient(circle at 50% 50%, #e8c27a 0%, #c9a060 38%, #9aa089 62%, rgba(255,255,255,0) 75%);
  }
  .product-band {
    position: absolute; left: 0; top: 212px; width: 445px; height: 168px;
  }
  .product-name {
    position: absolute; left: 98px; top: 212px; height: 168px;
    font-weight: 700; font-size: 168px; line-height: 168px;
    color: var(--label-white); letter-spacing: -6px;
    white-space: nowrap;
  }
  .form-band {
    position: absolute; left: 0; top: 380px; width: 440px; height: 30px;
    background: linear-gradient(90deg, var(--band-grey-light), var(--band-grey-dark) 80%, var(--band-grey-light));
    border-radius: 0 0 10px 0;
  }
  .form-name {
    position: absolute; left: 0; top: 380px; width: 440px; height: 30px;
    font-weight: 400; font-size: 26px; line-height: 32px; letter-spacing: 2px;
    font-variant: small-caps; color: var(--label-white); text-align: center;
    white-space: nowrap;
  }
  .features { list-style: none; position: absolute; top: 440px; left: 0; }
  .features li {
    position: relative; font-weight: 700; font-size: 26px; line-height: 38px;
    color: var(--text-orange); white-space: nowrap;
  }
  .features li::before {
    content: ""; position: absolute; left: -16px; top: 16px;
    width: 7px; height: 7px; background: var(--ink-grey);
  }
  .features li:nth-child(1) { margin-left: 132px; }
  .features li:nth-child(2) { margin-left: 150px; }
  .features li:nth-child(3) { margin-left: 167px; }
  .rule {
    position: absolute; left: 75px; top: 556px; width: 350px; height: 2px;
    background: var(--rule-grey);
  }
  .dosage {
    position: absolute; left: 110px; top: 568px;
    font-weight: 700; font-size: 22px; color: var(--ink-grey);
    white-space: nowrap;
  }
  .dosage .divider { margin: 0 12px; }
</style>
</head>
<body>
  <main class="label">
    <div class="brand-tab"></div>
    <div class="brand-mark"></div>
    <div class="brand-name">Corlen Sabo</div>

    <p class="claim">Supports Nerve Cells and Brain Tissue</p>
    <div class="brain-art" role="img" aria-label="Illustration of a glowing human brain"></div>

    <svg class="product-band" viewBox="0 0 445 168" aria-hidden="true">
      <polygon points="0,0 400,0 445,45 445,168 0,168" fill="var(--brand-orange)"/>
    </svg>
    <h1 class="product-name">B-12</h1>

    <div class="form-band"></div>
    <h2 class="form-name">Methycobalamin</h2>

    <ul class="features">
      <li>Sublingual</li>
      <li>Dietary Supplement</li>
      <li>Vegetarian</li>
    </ul>

    <div class="rule"></div>
    <p class="dosage">1000mcg<span class="divider">I</span>90 Lozenges</p>
  </main>
</body>
</html>
```